Thistle Root Organic

Please find attached screenshots of a same product as what I'm selling, looking for similar packaging but yet a whole new different design with my own logo rivertiles which is also attached. It will be on white bags with the clear on the bottom center. As far as colors maby green yellow and black or if you have a better idea. Also it needs to be something that looks up to date modern I like when it has that two-tone gloss to it where it goes from darker to lighter.

```html
<!DOCTYPE html>
<html lang="en">
<head>
<meta charset="UTF-8">
<title>Thistle Root Organic – Pouch Front</title>
<link href="https://fonts.googleapis.com/css2?family=Fredoka:wght@600&family=Montserrat:wght@500;600&display=swap" rel="stylesheet">
<style>
  :root {
    --page: #eceeea;
    --pouch-white: #ffffff;
    --pouch-shade: #e9ece6;
    --ink-black: #161616;
    --green-dark: #145a32;
    --green-mid: #2f8f3e;
    --green-light: #8cc63f;
    --yellow: #f2d230;
    --window-edge: #ffffff;
    --leaf-dark: #3d3a22;
    --leaf-mid: #6b6b3a;
    --leaf-light: #b5a765;
    --text-white: #ffffff;
  }
  html, body {
    margin: 0;
    width: 1200px;
    height: 1200px;
    overflow: hidden;
    background: var(--page);
  }
  .canvas {
    position: relative;
    width: 1200px;
    height: 1200px;
  }
  .pouch {
    position: absolute;
    left: 260px;
    top: 80px;
    width: 680px;
    height: 1000px;
    background: linear-gradient(100deg, var(--pouch-shade) 0%, var(--pouch-white) 45%, var(--pouch-shade) 100%);
    box-shadow: 0 10px 30px rgba(0, 0, 0, 0.12);
    overflow: hidden;
  }
  .zipper {
    position: absolute;
    left: 40px;
    right: 40px;
    top: 110px;
    height: 12px;
    border-top: 2px solid #d4d8d0;
    border-bottom: 2px solid #d4d8d0;
  }
  .brand {
    position: absolute;
    top: 200px;
    left: 0;
    right: 0;
    display: flex;
    align-items: center;
    justify-content: center;
    gap: 18px;
  }
  .brand-dot {
    width: 54px;
    height: 54px;
    border-radius: 50%;
    background: var(--green-mid);
  }
  .brand-name {
    font-family: "Montserrat", sans-serif;
    font-weight: 600;
    font-size: 40px;
    letter-spacing: 6px;
    color: var(--ink-black);
  }
  .product-title {
    position: absolute;
    top: 300px;
    left: 0;
    right: 0;
    margin: 0;
    text-align: center;
    font-family: "Fredoka", sans-serif;
    font-weight: 600;
    font-size: 76px;
    line-height: 1;
    color: var(--ink-black);
    letter-spacing: 1px;
  }
  .title-rule {
    position: absolute;
    top: 400px;
    left: 290px;
    width: 100px;
    height: 6px;
    border-radius: 3px;
    background: var(--yellow);
  }
  .color-band {
    position: absolute;
    left: 0;
    top: 0;
  }
  .net-weight {
    position: absolute;
    bottom: 0;
    left: 0;
    right: 0;
    height: 60px;
    line-height: 60px;
    text-align: center;
    background: var(--ink-black);
    font-family: "Montserrat", sans-serif;
    font-weight: 500;
    font-size: 18px;
    letter-spacing: 3px;
    color: var(--text-white);
  }
</style>
</head>
<body>
<div class="canvas">
  <div class="pouch">
    <div class="zipper"></div>

    <div class="brand">
      <div class="brand-dot"></div>
      <div class="brand-name">RIVERTILES</div>
    </div>

    <h1 class="product-title">THISTLE ROOT</h1>
    <div class="title-rule"></div>

    <svg class="color-band" width="680" height="1000" viewBox="0 0 680 1000">
      <defs>
        <linearGradient id="bandGloss" x1="0" y1="0" x2="1" y2="1">
          <stop offset="0%" stop-color="var(--green-dark)"/>
          <stop offset="55%" stop-color="var(--green-mid)"/>
          <stop offset="100%" stop-color="var(--green-light)"/>
        </linearGradient>
        <linearGradient id="accentGloss" x1="0" y1="0" x2="1" y2="0">
          <stop offset="0%" stop-color="var(--green-light)"/>
          <stop offset="100%" stop-color="var(--yellow)"/>
        </linearGradient>
        <radialGradient id="windowFill" cx="50%" cy="50%" r="60%">
          <stop offset="0%" stop-color="var(--leaf-mid)"/>
          <stop offset="70%" stop-color="var(--leaf-dark)"/>
          <stop offset="100%" stop-color="var(--leaf-light)"/>
        </radialGradient>
      </defs>
      <path d="M0 520 C200 470 460 470 680 540 L680 470 C460 400 200 410 0 470 Z" fill="url(#accentGloss)"/>
      <path d="M0 540 C200 490 460 490 680 560 L680 940 L0 940 Z" fill="url(#bandGloss)"/>
      <path role="img" aria-label="Clear window showing loose dried thistle root"
        d="M190 700 C190 640 250 610 340 610 C430 610 490 640 490 700 L490 880 C490 915 465 940 430 940 L250 940 C215 940 190 915 190 880 Z"
        fill="url(#windowFill)" fill-opacity="0.85" stroke="var(--window-edge)" stroke-width="6"/>
      <circle cx="560" cy="660" r="56" fill="var(--yellow)"/>
      <circle cx="560" cy="660" r="42" fill="none" stroke="var(--ink-black)" stroke-width="3"/>
    </svg>

    <div class="net-weight">NET WEIGHT 1.27 OZ. (36g)</div>
  </div>
</div>
</body>
</html>
```